Graphics Design of Physics Book

Hi
Size : 8" x 11.25"
We are education book Publication Company and would like to have book cover for "Physics" it has 4 volumes. All 4 having the same color scheme and design except the volume no.
Blue is my personal favorite but u can use any color. Want to have a band at the bottom of the cover to place our Logo “VORLIN Education” a PDF of the same is attached, or you can place logo anywhere according to ur design.
I need “Physics” as title of the book to be visible prominently.
And volume and volume no. should also be Visible and eye catching I prefer a Graphic to enhance the Volume No.
A background pattern can also be a option (it should be vector form so that color can be change later)
Please do not offer any cut and paste design I need very professional presentation.
Volume and Number can be in metallic 3D (CMYK) effect.
only Professional presentation will get feedback.
I have provided a sample artwork for reference do not follow it but can be a reference what I needed !

Target Market(s)

Students Class 9th to 12th

Industry/Entity Type

Education

Font styles to use
Serif

Colors
3176b5
0555a3
85abd2
cadf82
abd036
9bcb3c

Requirements
Must have
• Eye catching.
• “Physics” as title of the book to be visible prominently.
• volume and volume no. should also be Visible and eye catching
• I prefer a Graphic to enhance the Volume No.
• Icons for
• 1. Questions and answers
• 2. Theory Notes
• 3. Tips & Tricks
• 4. Previous Year's Reference Questions
• 5. Covers Complete Syllabus
Nice to have
• decent seamless background or metallic 3d effect (not to be print in special Ink) design should only be in CMYK.
Should not have
• Physics related Pictures or Icons (Specially E=mc2) or any scientist photograph or I Need pure graphic design

```html
<!DOCTYPE html>
<html lang="en">
<head>
<meta charset="utf-8">
<title>Physics 9 – Book Cover</title>
<link rel="stylesheet" href="https://fonts.googleapis.com/css2?family=Baloo+2:wght@800&family=Quicksand:wght@700&display=swap">
<style>
  :root {
    --page: #ffffff;
    --blue-light: #3fa3cf;
    --blue-mid: #2a86bb;
    --blue-deep: #2b4f86;
    --navy: #27206a;
    --teal: #12a393;
    --silver-hi: #f2f2f2;
    --silver-mid: #bdbdbd;
    --silver-lo: #8e8e8e;
    --green: #86b52a;
    --label: #1c1c3a;
    --ink: #111111;
  }
  html, body {
    margin: 0;
    padding: 0;
    width: 1200px;
    height: 1200px;
    overflow: hidden;
    background: var(--page);
  }
  .cover {
    display: block;
    width: 1200px;
    height: 1200px;
  }
  .title {
    font-family: "Baloo 2", "Arial Rounded MT Bold", sans-serif;
    font-weight: 800;
    fill: var(--navy);
    stroke: url(#silverStroke);
    stroke-width: 14;
    paint-order: stroke;
  }
  .volume-number {
    font-family: "Baloo 2", "Arial Rounded MT Bold", sans-serif;
    font-weight: 800;
    fill: url(#metalFill);
    stroke: #d9d9d9;
    stroke-width: 6;
    paint-order: stroke;
  }
  .feature-circle {
    fill: var(--green);
    stroke: #ffffff;
    stroke-width: 5;
  }
  .feature-glyph {
    fill: none;
    stroke: #ffffff;
    stroke-width: 5;
    stroke-linecap: round;
    stroke-linejoin: round;
  }
  .feature-glyph-text {
    font-family: "Quicksand", sans-serif;
    font-weight: 700;
    fill: #ffffff;
  }
  .feature-label {
    font-family: "Quicksand", sans-serif;
    font-weight: 700;
    font-size: 18px;
    fill: var(--label);
    text-anchor: middle;
  }
  .publisher-name {
    font-family: "Baloo 2", "Arial Rounded MT Bold", sans-serif;
    font-weight: 800;
    font-size: 46px;
    fill: var(--ink);
    text-anchor: middle;
    letter-spacing: 2px;
  }
</style>
</head>
<body>
<svg class="cover" viewBox="0 0 1500 1500" xmlns="http://www.w3.org/2000/svg" role="img" aria-label="Physics volume 9 book cover">
  <defs>
    <linearGradient id="silverBand" x1="0" y1="0" x2="1" y2="0">
      <stop offset="0" stop-color="#9c9c9c"/>
      <stop offset="0.1" stop-color="#e4e4e4"/>
      <stop offset="0.3" stop-color="#a9a9a9"/>
      <stop offset="0.5" stop-color="#dcdcdc"/>
      <stop offset="0.62" stop-color="#bdbdbd"/>
      <stop offset="0.75" stop-color="#9a9a9a"/>
      <stop offset="0.92" stop-color="#e0e0e0"/>
      <stop offset="1" stop-color="#c4c4c4"/>
    </linearGradient>
    <radialGradient id="blueField" cx="0.5" cy="0.45" r="0.7">
      <stop offset="0" stop-color="var(--blue-light)"/>
      <stop offset="0.6" stop-color="var(--blue-mid)"/>
      <stop offset="1" stop-color="var(--blue-deep)"/>
    </radialGradient>
    <linearGradient id="metalFill" x1="0" y1="0" x2="0" y2="1">
      <stop offset="0" stop-color="#f5f5f5"/>
      <stop offset="0.35" stop-color="#a8a8a8"/>
      <stop offset="0.5" stop-color="#5e5e5e"/>
      <stop offset="0.65" stop-color="#d8d8d8"/>
      <stop offset="1" stop-color="#9a9a9a"/>
    </linearGradient>
    <linearGradient id="silverStroke" x1="0" y1="0" x2="0" y2="1">
      <stop offset="0" stop-color="#e6e6e6"/>
      <stop offset="0.5" stop-color="#9a9a9a"/>
      <stop offset="1" stop-color="#d4d4d4"/>
    </linearGradient>
  </defs>

  <!-- cover base -->
  <rect class="silver-band" x="216" y="0" width="1070" height="1500" fill="url(#silverBand)"/>

  <!-- central blue field -->
  <path class="blue-field" role="img" aria-label="Blue background with diagonal stripe pattern"
        d="M216,200 L545,200 L600,150 L888,150 L945,200 L1286,200 L1286,1225 L955,1225 L900,1280 L610,1280 L555,1225 L216,1225 Z"
        fill="url(#blueField)"/>

  <!-- teal trims -->
  <polyline class="trim" points="216,175 545,175 600,125 888,125 945,175 1286,175" fill="none" stroke="var(--teal)" stroke-width="6"/>
  <polyline class="trim" points="216,1250 555,1250 610,1300 900,1300 955,1250 1286,1250" fill="none" stroke="var(--teal)" stroke-width="6"/>

  <!-- title -->
  <text class="title" x="750" y="485" font-size="250" text-anchor="middle" textLength="760" lengthAdjust="spacingAndGlyphs">Physics</text>

  <!-- volume number -->
  <text class="volume-number" x="748" y="862" font-size="380" text-anchor="middle">9</text>

  <!-- feature strip -->
  <rect class="feature-strip" x="216" y="1015" width="1070" height="172" fill="#b7a6d6" fill-opacity="0.45"/>
  <rect class="feature-strip-line" x="216" y="1028" width="1070" height="16" fill="#ffffff" fill-opacity="0.3"/>

  <!-- feature: questions -->
  <g class="feature">
    <circle class="feature-circle" cx="465" cy="1040" r="56"/>
    <text class="feature-glyph-text" x="465" y="1068" font-size="82" text-anchor="middle">?</text>
    <text class="feature-label" x="465" y="1124">Questions</text>
    <text class="feature-label" x="465" y="1146">and answers</text>
  </g>

  <!-- feature: theory notes -->
  <g class="feature">
    <circle class="feature-circle" cx="608" cy="1040" r="56"/>
    <rect class="feature-glyph" x="585" y="1010" width="44" height="56" rx="3"/>
    <rect class="feature-glyph" x="597" y="1003" width="20" height="10" rx="2"/>
    <line class="feature-glyph" x1="594" y1="1026" x2="620" y2="1026"/>
    <line class="feature-glyph" x1="594" y1="1038" x2="614" y2="1038"/>
    <path class="feature-glyph" d="M640,1030 L616,1058 L612,1068 L622,1063 L646,1036 Z"/>
    <text class="feature-label" x="604" y="1124">Theory Notes</text>
  </g>

  <!-- feature: tips -->
  <g class="feature">
    <circle class="feature-circle" cx="752" cy="1040" r="56"/>
    <path class="feature-glyph" d="M741,1058 C741,1048 733,1044 733,1032 A19,19 0 0 1 771,1032 C771,1044 763,1048 763,1058 Z"/>
    <line class="feature-glyph" x1="743" y1="1066" x2="761" y2="1066"/>
    <line class="feature-glyph" x1="745" y1="1074" x2="759" y2="1074"/>
    <line class="feature-glyph" x1="752" y1="1000" x2="752" y2="1005"/>
    <line class="feature-glyph" x1="726" y1="1012" x2="730" y2="1016"/>
    <line class="feature-glyph" x1="778" y1="1012" x2="774" y2="1016"/>
    <line class="feature-glyph" x1="720" y1="1032" x2="724" y2="1032"/>
    <line class="feature-glyph" x1="784" y1="1032" x2="780" y2="1032"/>
    <text class="feature-label" x="748" y="1124">Tips &amp; Tricks</text>
  </g>

  <!-- feature: previous years -->
  <g class="feature">
    <circle class="feature-circle" cx="896" cy="1040" r="56"/>
    <path class="feature-glyph" d="M905,1066 L905,1048 C905,1036 896,1028 884,1022" stroke-width="8"/>
    <path d="M874,1008 L896,1016 L880,1034 Z" fill="#ffffff"/>
    <text class="feature-label" x="890" y="1124">Previous Year's</text>
    <text class="feature-label" x="890" y="1146">Reference</text>
    <text class="feature-label" x="890" y="1168">Questions</text>
  </g>

  <!-- feature: syllabus -->
  <g class="feature">
    <circle class="feature-circle" cx="1040" cy="1040" r="56"/>
    <text class="feature-glyph-text" x="1040" y="1060" font-size="52" text-anchor="middle">La</text>
    <text class="feature-label" x="1038" y="1124">Covers</text>
    <text class="feature-label" x="1038" y="1146">Complete</text>
    <text class="feature-label" x="1038" y="1168">Syllabus</text>
  </g>

  <!-- publisher -->
  <text class="publisher-name" x="758" y="1398">VORLIN EDUCATION</text>
</svg>
</body>
</html>
```